Website for Apartment Rental in Prague

I would like to create designs of my website focused on luxury apartment rentals in Prague, Czech Republic. I created initial mock-ups, They are all attached. I need to design homepage and subpage. The mock-ups were created by combining elements from different websites that I liked but I need you to create a design that is unique and original. The attached files a only a guidance for the structure of the website but not for the design. Try to be creative.

Industry/Entity Type

Apartment

```html
<!DOCTYPE html>
<html lang="en">
<head>
<meta charset="utf-8">
<title>Belle Nuit Apartments Prague</title>
<link rel="stylesheet" href="https://fonts.googleapis.com/css2?family=Josefin+Sans:wght@400;600;700&family=Open+Sans:ital,wght@0,400;0,600;0,700;1,400&display=swap">
<style>
:root{
  --accent:#a47c66;
  --band:#3b3a39;
  --ink:#2e2e2e;
  --muted:#7a7a7a;
  --line:#d9d9d9;
  --paper:#ffffff;
}
*{box-sizing:border-box;margin:0;padding:0}
html,body{width:1200px;height:3509px;overflow:hidden}
body{position:relative;background:var(--paper);font-family:"Open Sans",Arial,sans-serif;color:var(--ink)}
.abs{position:absolute}

.topbar{left:0;top:0;width:1200px;height:24px;background:var(--accent);color:#fff;font-size:11px;font-weight:600;letter-spacing:.3px}
.topbar span{position:absolute;top:5px}

.brand{display:flex;align-items:center;gap:10px;font-family:"Josefin Sans",sans-serif;font-weight:700;color:var(--ink);white-space:nowrap}
.brand .mark{width:14px;height:14px;background:var(--accent)}
.search{left:709px;top:51px;width:390px;height:38px;border:1px solid var(--line);font-size:13px;color:#999;padding:10px 14px}
.search svg{position:absolute;right:12px;top:11px}
.nav{left:98px;top:112px;width:1001px;height:40px;display:flex;justify-content:space-between;align-items:center;font-family:"Josefin Sans",sans-serif;font-weight:600;font-size:15px;color:var(--ink)}

.hero{left:0;top:152px;width:1200px;height:421px;background:linear-gradient(90deg,#4d8c92 0,#d7d3cf 14%,#eeeae6 45%,#c8c1b9 70%,#e4e0dc 88%,#5a9aa0 100%)}
.hero-shade{left:0;top:152px;width:1200px;height:421px;background:linear-gradient(180deg,rgba(0,0,0,.05),rgba(0,0,0,.15) 60%,rgba(0,0,0,.05))}
.hero-title{left:0;top:300px;width:1200px;text-align:center;color:#fff;font-family:"Josefin Sans",sans-serif;font-weight:600;font-size:45px;letter-spacing:.5px;text-shadow:0 2px 8px rgba(0,0,0,.35)}
.hero-sub{left:0;top:360px;width:1200px;text-align:center;color:#fff;font-size:24px;font-weight:600;text-shadow:0 2px 6px rgba(0,0,0,.35)}
.arrow{top:352px}

.booking{left:0;top:573px;width:1200px;height:229px;background:var(--band)}
.booking-title{left:0;top:604px;width:1200px;text-align:center;color:#fff;font-family:"Josefin Sans",sans-serif;font-weight:600;font-size:24px;letter-spacing:.5px}
.field-label{top:650px;color:#fff;font-size:11px;font-weight:700;letter-spacing:.3px}
.field{top:676px;height:37px;background:#fff;font-size:12px;color:#555;padding:10px 8px;display:flex;align-items:center;gap:6px}
.field .drop{position:absolute;right:0;top:0;width:42px;height:100%;background:#ddd}
.field .drop svg{position:absolute;left:16px;top:15px}
.btn{display:inline-flex;align-items:center;justify-content:center;border-radius:22px;font-weight:700;font-size:13px;letter-spacing:.4px}
.btn-fill{background:var(--accent);color:#fff}
.btn-line{border:2px solid #d6cfc9;color:var(--accent);background:#fff}
.check{left:353px;top:732px;width:220px;height:42px;font-size:15px}
.or{left:590px;top:745px;color:#fff;font-size:12px;font-weight:700}
.unit{left:625px;top:734px;width:222px;height:38px}

.section-title{left:0;width:1200px;text-align:center;font-family:"Josefin Sans",sans-serif;font-weight:600;font-size:34px;letter-spacing:.5px;color:var(--ink)}
.welcome-text{left:187px;top:942px;width:826px;text-align:center;font-size:13px;line-height:24px;color:var(--muted)}
.about{left:529px;top:1076px;width:143px;height:47px;font-size:14px}
.divider{left:98px;top:1200px;width:1001px;height:2px;background:var(--line)}

.cards{left:98px;top:1343px;width:1001px;display:grid;grid-template-columns:repeat(3,318px);column-gap:23px;row-gap:54px}
.card-photo{height:201px}
.card-title{margin-top:26px;font-family:"Josefin Sans",sans-serif;font-weight:600;font-size:19px;line-height:26px}
.card-rule{height:2px;background:var(--line);margin-top:10px}
.card-text{margin-top:14px;font-size:12.5px;line-height:19px;color:var(--muted)}
.card-meta{margin-top:12px;font-size:12px;color:#555;display:flex;align-items:center;gap:6px}
.card-meta .sep{margin:0 12px;color:#999}
.card-actions{margin-top:17px;display:flex;gap:11px}
.card-actions .btn{height:42px}
.book{width:136px}
.details{width:147px}
.p1{background:linear-gradient(135deg,#5b5048,#d8d2cb 45%,#8a7d70)}
.p2{background:linear-gradient(135deg,#cfc6bb,#f1ede8 50%,#6f5a48)}
.p3{background:linear-gradient(135deg,#eceae6,#bdb3a8 55%,#6b5645)}
.p4{background:linear-gradient(135deg,#6a6461,#e6e3df 50%,#a39a92)}
.p5{background:linear-gradient(135deg,#efe9e2,#c9b9a8 55%,#7c6653)}
.p6{background:linear-gradient(135deg,#3f3a35,#b9a996 50%,#e8e2da)}
.more{left:489px;top:2370px;width:222px;height:46px;font-size:14px}

.testi-bg{left:0;top:2493px;width:1200px;height:333px;background:linear-gradient(90deg,#8c8784,#5f5c5a 45%,#4a4847)}
.testi-title{left:98px;top:2631px;color:#fff;font-family:"Josefin Sans",sans-serif;font-weight:600;font-size:33px;line-height:38px;letter-spacing:.5px}
.avatar{left:576px;top:2529px;width:102px;height:102px;border-radius:50%;border:4px solid #fff;background:linear-gradient(180deg,#c9c4bf,#8c857f)}
.testi-text{left:575px;top:2652px;width:525px;color:#fff;font-style:italic;font-size:15px;line-height:24px}
.testi-name{left:575px;top:2757px;color:#fff;font-size:13px;font-weight:700;letter-spacing:.5px}

.know-icon{width:94px;height:94px;border-radius:50%;border:2px solid var(--line);display:flex;align-items:center;justify-content:center;top:2975px}
.know-title{top:2981px;font-family:"Josefin Sans",sans-serif;font-weight:600;font-size:19px}
.know-text{top:3015px;width:190px;font-size:13px;line-height:21px;color:var(--muted)}

.footer-rule{left:0;top:3131px;width:1200px;height:6px;background:var(--accent)}
.foot-head{top:3201px;font-family:"Josefin Sans",sans-serif;font-weight:600;font-size:18px}
.foot-links{top:3245px;font-size:12px;line-height:25px;color:#555;list-style:none}
.foot-text{font-size:12px;line-height:20px;color:#555}
.email-field{left:547px;top:3303px;width:256px;height:32px;border-bottom:1px solid var(--line);font-size:12px;color:#777;padding-top:6px}
.subscribe{left:547px;top:3357px;width:108px;height:28px;font-size:11px;border-width:1px}
.contact-row{left:879px;display:flex;gap:14px}
.bottom-rule{left:98px;top:3443px;width:1001px;height:1px;background:var(--line)}
.copy{left:98px;top:3468px;font-size:12px;color:#555}
.social{top:3462px;width:28px;height:28px;border-radius:50%;border:1px solid #aaa}
</style>
</head>
<body>

<div class="abs topbar">
  <span style="left:98px">▪ OUR HOSPITALITY &nbsp;|&nbsp; EN ▾</span>
  <span style="left:563px">▪ DISCOVER PRAGUE</span>
  <span style="left:736px">✉ RESERVATION@BELLENUITSTAY.COM</span>
  <span style="left:980px">✆ + 420 600 118 204</span>
</div>

<div class="abs brand" style="left:98px;top:58px;font-size:24px"><span class="mark"></span>Belle Nuit</div>
<div class="abs search">Search
  <svg width="14" height="14" viewBox="0 0 14 14"><circle cx="6" cy="6" r="4.5" fill="none" stroke="#555" stroke-width="1.6"/><line x1="9.3" y1="9.3" x2="13" y2="13" stroke="#555" stroke-width="1.8"/></svg>
</div>
<nav class="abs nav">
  <span>APARTMENTS</span><span>LOCATION</span><span>SERVICES</span><span>GALLERY</span><span>NEWS</span><span>EXCLUSIVE OFFERS &amp; TOURS</span><span>FOR FAMILIES</span><span>CONTACT US</span>
</nav>

<div class="abs hero" role="img" aria-label="Photo of a bright luxury apartment living room with white sofa and fireplace"></div>
<div class="abs hero-shade"></div>
<div class="abs hero-title">BELLE NUIT APARTMENTS PRAGUE</div>
<div class="abs hero-sub">Luxury apartment rentals in Prague</div>
<svg class="abs arrow" style="left:10px" width="14" height="22" viewBox="0 0 14 22"><polyline points="11,2 3,11 11,20" fill="none" stroke="#fff" stroke-width="2.5"/></svg>
<svg class="abs arrow" style="left:1176px" width="14" height="22" viewBox="0 0 14 22"><polyline points="3,2 11,11 3,20" fill="none" stroke="#fff" stroke-width="2.5"/></svg>

<div class="abs booking"></div>
<div class="abs booking-title">OFFICIAL SITE - BEST PRACTICE GUARANTEED</div>
<div class="abs field-label" style="left:98px">CHECK IN DATE</div>
<div class="abs field-label" style="left:274px">CHECK OUT DATE</div>
<div class="abs field-label" style="left:451px">ADULTS</div>
<div class="abs field-label" style="left:568px">CHILDREN</div>
<div class="abs field-label" style="left:683px">INFANTS</div>
<div class="abs field-label" style="left:800px">PROMOTIONAL CODE</div>
<div class="abs field" style="left:98px;width:166px"><svg width="11" height="11" viewBox="0 0 11 11"><rect x=".5" y="1.5" width="10" height="9" fill="none" stroke="#777"/><rect x=".5" y="1.5" width="10" height="3" fill="#777"/></svg>11/17/2017</div>
<div class="abs field" style="left:274px;width:168px"><svg width="11" height="11" viewBox="0 0 11 11"><rect x=".5" y="1.5" width="10" height="9" fill="none" stroke="#777"/><rect x=".5" y="1.5" width="10" height="3" fill="#777"/></svg>11/17/2017</div>
<div class="abs field" style="left:451px;width:108px">2<div class="drop"><svg width="10" height="6"><polygon points="0,0 10,0 5,6" fill="#777"/></svg></div></div>
<div class="abs field" style="left:568px;width:106px">2<div class="drop"><svg width="10" height="6"><polygon points="0,0 10,0 5,6" fill="#777"/></svg></div></div>
<div class="abs field" style="left:683px;width:108px">0<div class="drop"><svg width="10" height="6"><polygon points="0,0 10,0 5,6" fill="#777"/></svg></div></div>
<div class="abs field" style="left:800px;width:299px"></div>
<div class="abs btn btn-fill check">CHECK AVAILABILITY</div>
<div class="abs or">OR</div>
<div class="abs field unit">Select Rental unit<div class="drop"><svg width="10" height="6"><polygon points="0,0 10,0 5,6" fill="#777"/></svg></div></div>

<h1 class="abs section-title" style="top:880px">WELCOME TO BELLE NUIT</h1>
<p class="abs welcome-text">At vero eos et accusamus et iusto odio dignissimos ducimus qui blanditiis praesentium voluptatum deleniti atque corrupti quos dolores et quas molestias excepturi sint occaecati cupiditate non provident, similique sunt in culpa qui officia deserunt mollitia animi, id est laborum et dolorum fuga. Et harum quidem rerum facilis est et expedita distinctio. Nam libero tempore, cum soluta nobis est eligendi optio cumque nihil impedit quo minus id quod maxime placeat facere possimus</p>
<div class="abs btn btn-line about">ABOUT US</div>
<div class="abs divider"></div>

<h2 class="abs section-title" style="top:1262px">FEATURED PROPERTIES</h2>
<div class="abs cards">
  <article class="card"><div class="card-photo p1" role="img" aria-label="Photo of a modern living room"></div><h3 class="card-title">Brand new luxury living stunning contemporary design</h3><div class="card-rule"></div><p class="card-text">Nam libero tempore, cum soluta nobis est eligenop-tio cumque nihil impedit quo min..</p><div class="card-meta"><svg width="13" height="11" viewBox="0 0 13 11"><rect y="4" width="13" height="5" fill="var(--accent)"/><rect y="1" width="3" height="10" fill="var(--accent)"/></svg><span>1 Bedroom</span><span class="sep">|</span><svg width="13" height="11" viewBox="0 0 13 11"><circle cx="4" cy="3" r="2.5" fill="var(--accent)"/><circle cx="9.5" cy="3.5" r="2" fill="var(--accent)"/><path d="M0 11q0-5 4-5t4 5zM7 11q0-4 3-4t3 4z" fill="var(--accent)"/></svg><span>Max 4 People</span></div><div class="card-actions"><span class="btn btn-fill book">BOOK NOW!</span><span class="btn btn-line details">VIEW DETAILS</span></div></article>
  <article class="card"><div class="card-photo p2" role="img" aria-label="Photo of a living room with fireplace"></div><h3 class="card-title">Brand new luxury living stunning contemporary design</h3><div class="card-rule"></div><p class="card-text">Nam libero tempore, cum soluta nobis est eligenop-tio cumque nihil impedit quo min..</p><div class="card-meta"><svg width="13" height="11" viewBox="0 0 13 11"><rect y="4" width="13" height="5" fill="var(--accent)"/><rect y="1" width="3" height="10" fill="var(--accent)"/></svg><span>1 Bedroom</span><span class="sep">|</span><svg width="13" height="11" viewBox="0 0 13 11"><circle cx="4" cy="3" r="2.5" fill="var(--accent)"/><circle cx="9.5" cy="3.5" r="2" fill="var(--accent)"/><path d="M0 11q0-5 4-5t4 5zM7 11q0-4 3-4t3 4z" fill="var(--accent)"/></svg><span>Max 4 People</span></div><div class="card-actions"><span class="btn btn-fill book">BOOK NOW!</span><span class="btn btn-line details">VIEW DETAILS</span></div></article>
  <article class="card"><div class="card-photo p3" role="img" aria-label="Photo of an open plan living area with kitchen"></div><h3 class="card-title">Brand new luxury living stunning contemporary design</h3><div class="card-rule"></div><p class="card-text">Nam libero tempore, cum soluta nobis est eligenop-tio cumque nihil impedit quo min..</p><div class="card-meta"><svg width="13" height="11" viewBox="0 0 13 11"><rect y="4" width="13" height="5" fill="var(--accent)"/><rect y="1" width="3" height="10" fill="var(--accent)"/></svg><span>1 Bedroom</span><span class="sep">|</span><svg width="13" height="11" viewBox="0 0 13 11"><circle cx="4" cy="3" r="2.5" fill="var(--accent)"/><circle cx="9.5" cy="3.5" r="2" fill="var(--accent)"/><path d="M0 11q0-5 4-5t4 5zM7 11q0-4 3-4t3 4z" fill="var(--accent)"/></svg><span>Max 4 People</span></div><div class="card-actions"><span class="btn btn-fill book">BOOK NOW!</span><span class="btn btn-line details">VIEW DETAILS</span></div></article>
  <article class="card"><div class="card-photo p4" role="img" aria-label="Photo of a spacious lounge with large windows"></div><h3 class="card-title">Brand new luxury living stunning contemporary design</h3><div class="card-rule"></div><p class="card-text">Nam libero tempore, cum soluta nobis est eligenop-tio cumque nihil impedit quo min..</p><div class="card-meta"><svg width="13" height="11" viewBox="0 0 13 11"><rect y="4" width="13" height="5" fill="var(--accent)"/><rect y="1" width="3" height="10" fill="var(--accent)"/></svg><span>1 Bedroom</span><span class="sep">|</span><svg width="13" height="11" viewBox="0 0 13 11"><circle cx="4" cy="3" r="2.5" fill="var(--accent)"/><circle cx="9.5" cy="3.5" r="2" fill="var(--accent)"/><path d="M0 11q0-5 4-5t4 5zM7 11q0-4 3-4t3 4z" fill="var(--accent)"/></svg><span>Max 4 People</span></div><div class="card-actions"><span class="btn btn-fill book">BOOK NOW!</span><span class="btn btn-line details">VIEW DETAILS</span></div></article>
  <article class="card"><div class="card-photo p5" role="img" aria-label="Photo of a bright room with wooden floor"></div><h3 class="card-title">Brand new luxury living stunning contemporary design</h3><div class="card-rule"></div><p class="card-text">Nam libero tempore, cum soluta nobis est eligenop-tio cumque nihil impedit quo min..</p><div class="card-meta"><svg width="13" height="11" viewBox="0 0 13 11"><rect y="4" width="13" height="5" fill="var(--accent)"/><rect y="1" width="3" height="10" fill="var(--accent)"/></svg><span>1 Bedroom</span><span class="sep">|</span><svg width="13" height="11" viewBox="0 0 13 11"><circle cx="4" cy="3" r="2.5" fill="var(--accent)"/><circle cx="9.5" cy="3.5" r="2" fill="var(--accent)"/><path d="M0 11q0-5 4-5t4 5zM7 11q0-4 3-4t3 4z" fill="var(--accent)"/></svg><span>Max 4 People</span></div><div class="card-actions"><span class="btn btn-fill book">BOOK NOW!</span><span class="btn btn-line details">VIEW DETAILS</span></div></article>
  <article class="card"><div class="card-photo p6" role="img" aria-label="Photo of a living room with dark wood floor and fireplace"></div><h3 class="card-title">Brand new luxury living stunning contemporary design</h3><div class="card-rule"></div><p class="card-text">Nam libero tempore, cum soluta nobis est eligenop-tio cumque nihil impedit quo min..</p><div class="card-meta"><svg width="13" height="11" viewBox="0 0 13 11"><rect y="4" width="13" height="5" fill="var(--accent)"/><rect y="1" width="3" height="10" fill="var(--accent)"/></svg><span>1 Bedroom</span><span class="sep">|</span><svg width="13" height="11" viewBox="0 0 13 11"><circle cx="4" cy="3" r="2.5" fill="var(--accent)"/><circle cx="9.5" cy="3.5" r="2" fill="var(--accent)"/><path d="M0 11q0-5 4-5t4 5zM7 11q0-4 3-4t3 4z" fill="var(--accent)"/></svg><span>Max 4 People</span></div><div class="card-actions"><span class="btn btn-fill book">BOOK NOW!</span><span class="btn btn-line details">VIEW DETAILS</span></div></article>
</div>
<div class="abs btn btn-line more">VIEW MORE PROPERTY</div>

<div class="abs testi-bg" role="img" aria-label="Faded photo of an apartment interior"></div>
<svg class="abs" style="left:0;top:2493px" width="1200" height="333" viewBox="0 0 1200 333">
  <polygon points="0,0 620,0 258,333 0,110" fill="var(--accent)" opacity=".95"/>
  <g transform="rotate(180 139.5 66)"><path d="M100 34h34v30q0 22-18 34l-7-9q12-8 12-21h-21z M145 34h34v30q0 22-18 34l-7-9q12-8 12-21h-21z" fill="#fff"/></g>
</svg>
<div class="abs testi-title">CLIENT<br>TESTIMONIALS</div>
<div class="abs avatar" role="img" aria-label="Portrait of the reviewing guest"></div>
<p class="abs testi-text">Nam libero tempore, cum soluta nobis est eligendi optio cumque nihil ipedit quo minus id quod maxime placeat facere possimus, omnis voluptas assum enda est, omnis dolor repellendus.</p>
<div class="abs testi-name">- MARTIN K. HOLLOWAY MD,PA</div>
<svg class="abs" style="left:1056px;top:2773px" width="44" height="12" viewBox="0 0 44 12"><circle cx="6" cy="6" r="4.5" fill="#fff"/><circle cx="20" cy="6" r="4" fill="none" stroke="#fff" stroke-width="1.3"/><circle cx="34" cy="6" r="4" fill="none" stroke="#fff" stroke-width="1.3"/></svg>

<h2 class="abs section-title" style="top:2901px">NEED TO KNOW</h2>
<div class="abs know-icon" style="left:98px"><svg width="34" height="38" viewBox="0 0 34 38" fill="none" stroke="var(--accent)" stroke-width="2"><rect x="6" y="2" width="22" height="34"/><path d="M11 8h4M19 8h4M11 15h4M19 15h4M11 22h4M19 22h4M14 36v-7h6v7"/></svg></div>
<div class="abs know-title" style="left:217px">APARTMENTS</div>
<p class="abs know-text" style="left:217px">At vero eos et accusamus et iusto odio dignissimos.</p>
<div class="abs know-icon" style="left:446px"><svg width="36" height="36" viewBox="0 0 36 36" fill="none" stroke="var(--accent)" stroke-width="2"><rect x="3" y="6" width="30" height="27"/><path d="M3 13h30M10 2v8M26 2v8M9 19h4M16 19h4M23 19h4M9 26h4M16 26h4M23 26h4"/></svg></div>
<div class="abs know-title" style="left:564px">CHECK - OUT</div>
<p class="abs know-text" style="left:564px">At vero eos et accusamus et iusto odio dignissimos.</p>
<div class="abs know-icon" style="left:802px"><svg width="38" height="38" viewBox="0 0 38 38" fill="none" stroke="var(--accent)" stroke-width="2"><path d="M4 4h15l15 15-15 15L4 19z"/><circle cx="12" cy="12" r="3"/></svg></div>
<div class="abs know-title" style="left:921px">RATES</div>
<p class="abs know-text" style="left:921px">At vero eos et accusamus et iusto odio dignissimos.</p>

<div class="abs footer-rule"></div>
<div class="abs brand" style="left:98px;top:3290px;font-size:30px"><span class="mark" style="width:18px;height:18px"></span>Belle Nuit</div>
<div class="abs foot-head" style="left:349px">INFORMATION</div>
<ul class="abs foot-links" style="left:349px"><li>Help</li><li>FAQ</li><li>Support</li><li>Sitemap</li><li>Terms Of Use</li><li>Privacy Statement</li></ul>
<div class="abs foot-head" style="left:547px">NEWSLETTER SUBSCRIPTION</div>
<p class="abs foot-text" style="left:547px;top:3245px;width:260px">Register your Email Address to get information about us</p>
<div class="abs email-field">Email Address</div>
<div class="abs btn btn-line subscribe">SUBSCRIBE</div>
<div class="abs foot-head" style="left:879px">CONTACT US</div>
<div class="abs contact-row" style="top:3247px"><svg width="12" height="16" viewBox="0 0 12 16"><path d="M6 1a5 5 0 0 1 5 5c0 4-5 9-5 9S1 10 1 6a5 5 0 0 1 5-5z" fill="var(--muted)"/><circle cx="6" cy="6" r="2" fill="#fff"/></svg><p class="foot-text" style="line-height:23px;margin-top:-4px">48 Linden Court Avenue,<br>Suite 310 • Pasadena,<br>California 91107</p></div>
<div class="abs contact-row" style="top:3328px"><svg width="14" height="14" viewBox="0 0 14 14"><path d="M3 1l2.5 3-1.5 1.5q1.5 3 4.5 4.5L10 8.5l3 2.5-1.5 2Q5 12 1 2.5z" fill="var(--muted)"/></svg><p class="foot-text" style="margin-top:-3px">+ 420 600 118 204</p></div>
<div class="abs contact-row" style="top:3371px"><svg width="14" height="11" viewBox="0 0 14 11"><rect width="14" height="11" fill="var(--muted)"/><polyline points="0,0 7,6 14,0" fill="none" stroke="#fff" stroke-width="1.2"/></svg><p class="foot-text" style="margin-top:-5px">reservation@bellenuitstay.com</p></div>
<div class="abs bottom-rule"></div>
<div class="abs copy">Copyrights © 2017, Belle Nuit . All rights reserved.</div>
<div class="abs social" style="left:1039px"></div>
<div class="abs social" style="left:1073px"></div>

</body>
</html>
```